Financial Planning Business needs a business card design

We need a business card design that is for a new financial planning business based in Australia. We provide financial planning advice such as retirement planning, wealth creation, asset protection.

Attached is the logo design. On the front side of the business card needs to incorporate the following:
- adviser name
- adviser title (ie Managing Director)
- address
- phone number
- email
- website address

Ideally it should also have the business name and logo

On the back of the card I would like this to be black in colour with the business name and logo

I have been advised the font is "Cinzel" (regular and bold)

Industry/Entity Type

Financial

Requirements
Must have
• Logo and business name

Format to have as follows:
Ben xxxxxxxx
Managing Director / Senior Financial Adviser
address
phone email
website

```html
<!DOCTYPE html>
<html lang="en">
<head>
<meta charset="utf-8">
<title>Harbourline Wealth Planning – Business Card</title>
<link rel="stylesheet" href="https://fonts.googleapis.com/css2?family=Cinzel:wght@400;700&family=Open+Sans:wght@400;600;700&display=swap">
<style>
  :root {
    --brand-blue: #0b9ad6;
    --charcoal: #2e3033;
    --back-black: #111213;
    --mid-grey: #9a9c9e;
    --text-grey: #3c3d3f;
    --paper: #ffffff;
    --stage: #eceae6;
  }
  * { box-sizing: border-box; margin: 0; padding: 0; }
  html, body { width: 1200px; height: 720px; overflow: hidden; }
  body {
    background: var(--stage);
    font-family: "Open Sans", Arial, sans-serif;
    position: relative;
  }
  .card {
    position: absolute;
    top: 200px;
    width: 540px;
    height: 309px;
    overflow: hidden;
    box-shadow: 0 2px 8px rgba(0,0,0,0.12);
  }

  /* Front */
  .card-front { left: 40px; background: var(--paper); }
  .edge-band {
    position: absolute; left: 0; top: 0; width: 14px; height: 100%;
    background: linear-gradient(to bottom, transparent 0 18%, var(--brand-blue) 18% 52%, var(--charcoal) 52% 100%);
  }
  .wordmark {
    position: absolute; left: 42px; top: 40px;
    display: flex; align-items: center; gap: 14px;
  }
  .wordmark-square {
    width: 46px; height: 46px; background: var(--mid-grey);
  }
  .wordmark-name {
    font-family: "Cinzel", Georgia, serif;
    font-weight: 400;
    color: var(--brand-blue);
    line-height: 1.05;
  }
  .wordmark-name .line-main { display: block; font-size: 34px; letter-spacing: 1px; }
  .wordmark-name .line-sub { display: block; font-size: 17px; letter-spacing: 1.5px; }
  .holder {
    position: absolute; right: 30px; top: 122px; text-align: right;
  }
  .holder-name { font-weight: 700; font-size: 17px; color: var(--brand-blue); }
  .holder-title { font-size: 12px; color: var(--mid-grey); margin-top: 2px; }
  .contact-list {
    position: absolute; left: 40px; top: 186px; list-style: none;
    font-size: 13px; color: var(--text-grey);
  }
  .contact-list li { display: flex; align-items: center; gap: 8px; height: 20px; }
  .contact-list svg { width: 13px; height: 13px; flex: none; }
  .address {
    position: absolute; left: 40px; top: 272px;
    font-size: 13px; color: var(--text-grey);
  }

  /* Back */
  .card-back {
    left: 620px; background: var(--back-black);
    display: flex; flex-direction: column; align-items: center; justify-content: center;
  }
  .back-wordmark {
    display: flex; align-items: center; gap: 16px; margin-top: -20px;
  }
  .back-square { width: 56px; height: 56px; background: var(--mid-grey); }
  .back-name {
    font-family: "Cinzel", Georgia, serif; font-weight: 400;
    color: var(--paper); line-height: 1.1;
  }
  .back-name .line-main { display: block; font-size: 34px; letter-spacing: 1px; }
  .back-name .line-sub { display: block; font-size: 17px; letter-spacing: 1.5px; }
  .back-web {
    position: absolute; bottom: 44px; width: 100%; text-align: center;
    color: var(--paper); font-size: 15px; letter-spacing: 1.5px;
  }
</style>
</head>
<body>
  <section class="card card-front" aria-label="Business card front">
    <div class="edge-band"></div>
    <div class="wordmark">
      <div class="wordmark-square"></div>
      <div class="wordmark-name">
        <span class="line-main">Harbourline</span>
        <span class="line-sub">Wealth Planning</span>
      </div>
    </div>
    <div class="holder">
      <div class="holder-name">Your Name</div>
      <div class="holder-title">Title</div>
    </div>
    <ul class="contact-list">
      <li>
        <svg viewBox="0 0 14 14"><circle cx="7" cy="7" r="7" fill="var(--brand-blue)"/><path d="M4.5 3.5l1.5 0 .6 2-1 .7a5 5 0 0 0 2.2 2.2l.7-1 2 .6v1.5a1 1 0 0 1-1 1A6 6 0 0 1 3.5 4.5a1 1 0 0 1 1-1z" fill="#fff"/></svg>
        012-345-6789
      </li>
      <li>
        <svg viewBox="0 0 14 14"><circle cx="7" cy="7" r="7" fill="var(--brand-blue)"/><rect x="5" y="3" width="4" height="8" rx="0.8" fill="#fff"/></svg>
        012-345-6789
      </li>
      <li>
        <svg viewBox="0 0 14 14"><circle cx="7" cy="7" r="7" fill="var(--brand-blue)"/><rect x="3.5" y="4.5" width="7" height="5" fill="#fff"/><path d="M3.5 4.5L7 7.3l3.5-2.8" stroke="var(--brand-blue)" stroke-width="0.8" fill="none"/></svg>
        info@harbourlinewealth.com
      </li>
      <li>
        <svg viewBox="0 0 14 14"><circle cx="7" cy="7" r="7" fill="var(--brand-blue)"/><circle cx="7" cy="7" r="3.6" stroke="#fff" stroke-width="0.9" fill="none"/><path d="M3.4 7h7.2M7 3.4c-1.6 2-1.6 5.2 0 7.2M7 3.4c1.6 2 1.6 5.2 0 7.2" stroke="#fff" stroke-width="0.8" fill="none"/></svg>
        www.harbourlinewealth.com
      </li>
    </ul>
    <p class="address">Street Name, City Name, Zip Code - 000000</p>
  </section>

  <section class="card card-back" aria-label="Business card back">
    <div class="back-wordmark">
      <div class="back-square"></div>
      <div class="back-name">
        <span class="line-main">Harbourline</span>
        <span class="line-sub">Wealth Planning</span>
      </div>
    </div>
    <p class="back-web">www.harbourlinewealth.com</p>
  </section>
</body>
</html>
```